Professional looking Unforgettable Truck Wrap Design

We are looking for a wrap design for a growing landscape company. We just purchased new trucks and are looking to use our logo in the best way possible so show off who we are and what we do. We want it to be unforgettable and when someone sees our trucks, they know who we are without having to read our name.
We like the colors in our logo, we are more leaning towards larger logos on the sides of the vehicle, and a tailgate logo as well, and not really the full wraps, but maybe open to full wraps.

We are a full service landscape company located in Salt Lake City, Ut, we offer anything from Maintenance, to installation and sprinkler repair.

The trucks we will be getting, are 2021 Varnholt 7200 HD crew cabs
we will also have 2021 Varny Meridale crew cab trucks that I need logos on as well.

We would like to have our phone Number and Website listed on the truck as well as our USDOT # See below in the must haves for the information.
Updates

Sick

Industry/Entity Type

Landscaping

Requirements
Must have
• good flow on the truck
bold looking
Clear information

Phone Number 555-013-2768
Website www.fernbrookgroundworks.com
USDOT #7481926
Nice to have
• I have uploaded an image of a trailer we currently have, it has our old logo, but we really like the landscape design background so maybe if we could use something similar.

```html
<!DOCTYPE html>
<html lang="en">
<head>
<meta charset="utf-8">
<title>Fernbrook Truck Wrap – Side Panel</title>
<link rel="stylesheet" href="https://fonts.googleapis.com/css2?family=Montserrat:wght@600&family=Roboto+Condensed:wght@700&family=Roboto:wght@700&display=swap">
<style>
  :root {
    --canvas-grey: #bdc0c8;
    --wrap-white: #eef2f6;
    --sky-blue: #1ea6de;
    --ocean-blue: #0a84c4;
    --deep-blue: #12479c;
    --navy-band: #1a4b9a;
    --logo-blue: #2481c6;
    --ink: #000000;
    --paper: #ffffff;
  }
  html, body {
    margin: 0;
    width: 1200px;
    height: 1200px;
    overflow: hidden;
    background: var(--canvas-grey);
  }
  .wrap-layout {
    position: absolute;
    left: 50px;
    top: 460px;
    width: 1100px;
    height: 280px;
  }
  .brand-name {
    font-family: "Montserrat", sans-serif;
    font-weight: 600;
    font-size: 20px;
    fill: var(--logo-blue);
  }
  .headline {
    font-family: "Roboto Condensed", sans-serif;
    font-weight: 700;
    font-size: 25px;
    fill: var(--paper);
    stroke: var(--ink);
    stroke-width: 4px;
    paint-order: stroke;
    stroke-linejoin: round;
  }
  .phone {
    font-family: "Roboto", sans-serif;
    font-weight: 700;
    font-size: 38px;
    fill: var(--paper);
    stroke: var(--ink);
    stroke-width: 5px;
    paint-order: stroke;
    stroke-linejoin: round;
  }
  .website {
    font-family: "Roboto Condensed", sans-serif;
    font-weight: 700;
    font-size: 19px;
    fill: var(--paper);
    stroke: var(--ink);
    stroke-width: 3px;
    paint-order: stroke;
    stroke-linejoin: round;
  }
  .services {
    font-family: "Roboto Condensed", sans-serif;
    font-weight: 700;
    font-size: 14px;
    fill: var(--paper);
  }
</style>
</head>
<body>
<svg class="wrap-layout" viewBox="0 0 1100 280" role="img" aria-label="Fernbrook Lawn Care and Landscape truck side wrap layout">
  <defs>
    <linearGradient id="cab-fade" x1="0" y1="0" x2="0" y2="1">
      <stop offset="0" stop-color="var(--sky-blue)"/>
      <stop offset="0.45" stop-color="#bfe3f4"/>
      <stop offset="1" stop-color="var(--wrap-white)"/>
    </linearGradient>
    <linearGradient id="bed-blue" x1="0" y1="0" x2="1" y2="0">
      <stop offset="0" stop-color="var(--ocean-blue)"/>
      <stop offset="1" stop-color="var(--sky-blue)"/>
    </linearGradient>
    <clipPath id="panel-clip">
      <rect x="0" y="0" width="1100" height="280" rx="14"/>
    </clipPath>
  </defs>

  <g clip-path="url(#panel-clip)">
    <rect class="cab-area" x="0" y="0" width="1100" height="280" fill="url(#cab-fade)"/>
    <rect class="bed-area" x="650" y="0" width="450" height="280" fill="url(#bed-blue)"/>
    <path class="sweep-curve" d="M540 0 H650 V280 H500 C410 240 400 120 470 50 C490 30 515 12 540 0 Z" fill="var(--deep-blue)"/>
    <path class="sweep-curve-soft" d="M650 0 V280 H580 C565 190 600 90 650 0 Z" fill="var(--ocean-blue)" opacity="0.35"/>
    <rect class="service-band" x="878" y="102" width="41" height="178" fill="var(--navy-band)"/>
  </g>

  <g class="brand-lockup">
    <circle cx="350" cy="158" r="18" fill="var(--logo-blue)"/>
    <text class="brand-name" x="350" y="210" text-anchor="middle" textLength="137" lengthAdjust="spacingAndGlyphs">FERNBROOK</text>
  </g>

  <g class="contact-block">
    <text class="headline" x="464" y="142" textLength="308" lengthAdjust="spacingAndGlyphs">LAWN CARE AND LANDSCAPE</text>
    <text class="phone" x="464" y="183" textLength="245" lengthAdjust="spacingAndGlyphs">555-013-2768</text>
    <text class="website" x="464" y="205" textLength="247" lengthAdjust="spacingAndGlyphs">www.fernbrookgroundworks.com</text>
  </g>

  <text class="services" x="801" y="142" textLength="235" lengthAdjust="spacingAndGlyphs">MAINTENANCE&#160;&#160;&#160;INSTALLATION&#160;&#160;REPAIR</text>
</svg>
</body>
</html>
```